Watch brand needs new business cards

Kestrel Timepiece Company are looking for a new business card design incorporating our logo and brand colours as per our website.

Design should be 90x55mm with 3mm print margin from edges and 3mm external bleed.

Card should be double sided, e.g. logo one side, personal details on the other.

Logo will be provided as a vector.

The card must be able to show:
- Staff name
- Position
- Office Address
- Email
- Telephone number
- Website address

Final work must be provided in an editable format to allow us to add staff details (e.g. an AI or PSD file).

```html
<!DOCTYPE html>
<html lang="en">
<head>
<meta charset="utf-8">
<title>Kestrel Timepiece Company – Business Card</title>
<link rel="stylesheet" href="https://fonts.googleapis.com/css2?family=Cormorant+Garamond:wght@500;600&family=Josefin+Sans:wght@600&display=swap">
<style>
  :root {
    --backdrop: #d3d8d8;
    --card: #f1f0ec;
    --card-edge: #e2e0da;
    --gold: #a6852b;
    --gold-soft: #b89a45;
  }
  * { margin: 0; padding: 0; box-sizing: border-box; }
  html, body {
    width: 1200px;
    height: 823px;
    overflow: hidden;
    background: var(--backdrop);
  }
  .canvas {
    position: relative;
    width: 1200px;
    height: 823px;
    display: flex;
    align-items: center;
    justify-content: center;
    gap: 60px;
  }
  .card {
    position: relative;
    width: 500px;
    height: 306px;
    background: var(--card);
    border: 1px solid var(--card-edge);
    box-shadow: 0 10px 24px rgba(80, 90, 90, 0.18);
    color: var(--gold);
  }

  /* Brand lockup */
  .brand {
    display: flex;
    flex-direction: column;
    align-items: center;
    gap: 10px;
  }
  .brand-mark {
    border: 3px solid var(--gold);
    border-radius: 50%;
  }
  .brand-name {
    font-family: "Cormorant Garamond", serif;
    font-weight: 600;
    text-transform: uppercase;
    letter-spacing: 0.06em;
    text-align: center;
    line-height: 1.1;
    color: var(--gold);
  }

  /* Front: personal details */
  .card-front .brand {
    position: absolute;
    left: 38px;
    top: 40px;
    width: 170px;
  }
  .card-front .brand-mark { width: 98px; height: 98px; }
  .card-front .brand-name { font-size: 17px; }

  .details {
    position: absolute;
    right: 34px;
    top: 44px;
    text-align: right;
  }
  .staff-name {
    font-family: "Josefin Sans", sans-serif;
    font-weight: 600;
    font-size: 24px;
    letter-spacing: 0.08em;
    line-height: 1;
  }
  .staff-role {
    font-family: "Josefin Sans", sans-serif;
    font-weight: 600;
    font-size: 10px;
    letter-spacing: 0.14em;
    margin-top: 4px;
  }
  .address, .contact {
    font-family: "Cormorant Garamond", serif;
    font-weight: 500;
    font-size: 16px;
    line-height: 1.2;
    letter-spacing: 0.03em;
    font-style: normal;
  }
  .address { margin-top: 26px; }
  .contact { margin-top: 14px; list-style: none; }

  /* Back: logo side */
  .card-back {
    display: flex;
    align-items: center;
    justify-content: center;
  }
  .card-back .brand-mark { width: 58px; height: 58px; border-width: 2px; }
  .card-back .brand-name { font-size: 24px; }
</style>
</head>
<body>
<main class="canvas">

  <section class="card card-front" aria-label="Business card front">
    <div class="brand">
      <span class="brand-mark" aria-hidden="true"></span>
      <p class="brand-name">Kestrel Timepiece Company</p>
    </div>

    <div class="details">
      <h1 class="staff-name">YOUR NAME HERE</h1>
      <p class="staff-role">ASSISTANT MANAGER</p>
      <address class="address">
        1234 Street Avenue<br>
        New York City 0000
      </address>
      <ul class="contact">
        <li>(000)-000-0000</li>
        <li>(000)-000-0000</li>
        <li>support@maildomain.com</li>
        <li>www.yourwebsitehere.com</li>
      </ul>
    </div>
  </section>

  <section class="card card-back" aria-label="Business card back">
    <div class="brand">
      <span class="brand-mark" aria-hidden="true"></span>
      <p class="brand-name">Kestrel Timepiece Company</p>
    </div>
  </section>

</main>
</body>
</html>
```